Elementary School Snapshot of a Wayfinch

Please recreate a poster of our Snapshot of a Wayfinch traits that we desire to have when they graduate from 4th grade. This should be kid-friendly and kid-themed with icons to help communicate the Competencies. See attached six competencies and the "I can" statements next to. Our colors are navy, red and white. Our logo is attached as well. This will be made into a poster and displayed in each classroom, the office, and also used on social media.

```html
<!DOCTYPE html>
<html lang="en">
<head>
<meta charset="utf-8">
<title>Snapshot of a Wayfinch – Harbor Ridge Public Schools</title>
<link href="https://fonts.googleapis.com/css2?family=Archivo+Black&family=Barlow+Condensed:wght@500;600;700&display=swap" rel="stylesheet">
<style>
  :root {
    --navy: #141a4e;
    --red: #a01c24;
    --white: #ffffff;
    --backdrop: #bcbdc0;
    --ink: #141414;
  }
  * { box-sizing: border-box; margin: 0; padding: 0; }
  html, body { width: 848px; height: 1200px; overflow: hidden; }
  body { background: var(--backdrop); position: relative; font-family: "Barlow Condensed", "Arial Narrow", sans-serif; }

  .poster { position: absolute; left: 72px; top: 101px; width: 705px; height: 998px; background: var(--white); }

  .brand-mark { position: absolute; left: 150px; top: 44px; width: 110px; height: 110px; border-radius: 50%; background: var(--red); }
  .brand-name {
    position: absolute; left: 328px; top: 62px;
    font-family: "Barlow Condensed", "Arial Narrow", sans-serif;
    font-weight: 700; font-size: 56px; line-height: 54px; color: var(--navy);
    letter-spacing: -0.5px;
  }

  .level-band {
    position: absolute; left: 0; top: 183px; width: 705px; height: 48px;
    background: var(--red); color: var(--white);
    font-weight: 700; font-size: 36px; line-height: 48px; text-align: center;
  }

  .snapshot-title { position: absolute; left: 36px; top: 302px; width: 62px; height: 584px; }
  .snapshot-title text { font-family: "Archivo Black", "Arial Black", sans-serif; font-size: 62px; fill: var(--navy); }

  .trait {
    position: absolute; left: 107px; width: 563px;
    border: 2px solid var(--red); border-radius: 8px;
    padding: 20px 12px 0 16px;
  }
  .trait-name {
    position: absolute; left: 12px; top: -17px; padding: 0 4px 0 2px;
    background: var(--white); color: var(--red);
    font-weight: 700; font-size: 30px; line-height: 30px;
  }
  .trait-icon {
    position: absolute; right: 14px; top: -16px; width: 30px; height: 30px;
    background: var(--white);
  }
  .trait-icon svg { display: block; width: 30px; height: 30px; }
  .trait-icon .ring { fill: var(--white); stroke: var(--red); stroke-width: 2; }
  .trait-icon .glyph { fill: none; stroke: var(--navy); stroke-width: 2; stroke-linecap: round; stroke-linejoin: round; }
  .trait-icon .solid { fill: var(--navy); stroke: none; }

  .trait-list { list-style: none; }
  .trait-list li {
    position: relative; padding-left: 12px;
    font-weight: 600; font-size: 19.5px; line-height: 20.4px; color: var(--ink);
    letter-spacing: -0.2px;
  }
  .trait-list li.bulleted::before {
    content: ""; position: absolute; left: 0; top: 8px;
    width: 5px; height: 5px; border-radius: 50%; background: var(--ink);
  }

  .trait--communicator { top: 254px; height: 113px; }
  .trait--thinker { top: 388px; height: 112px; }
  .trait--responsible { top: 521px; height: 100px; padding-top: 27px; }
  .trait--adaptable { top: 635px; height: 96px; }
  .trait--collaborator { top: 748px; height: 96px; }
  .trait--compassionate { top: 861px; height: 97px; }
</style>
</head>
<body>
  <main class="poster">
    <div class="brand-mark" aria-hidden="true"></div>
    <h1 class="brand-name">Harbor Ridge<br>Public Schools</h1>

    <div class="level-band">Early learners and Elementary School</div>

    <svg class="snapshot-title" viewBox="0 0 62 584" aria-label="Snapshot of a Wayfinch">
      <text transform="translate(54 584) rotate(-90)" textLength="584" lengthAdjust="spacingAndGlyphs">Snapshot of a Wayfinch</text>
    </svg>

    <section class="trait trait--communicator">
      <h2 class="trait-name">Communicator</h2>
      <span class="trait-icon" aria-hidden="true"><svg viewBox="0 0 30 30"><circle class="ring" cx="15" cy="15" r="14"/><path class="glyph" d="M8 10h14v8h-8l-4 3v-3H8z"/></svg></span>
      <ul class="trait-list">
        <li class="bulleted">I can use words, writing, and pictures to clearly share ideas.</li>
        <li class="bulleted">I can look at the speaker and listen carefully to understand<br>what they are saying.</li>
        <li class="bulleted">I know how to adjust my communication for different places and people.</li>
      </ul>
    </section>

    <section class="trait trait--thinker">
      <h2 class="trait-name">Critical Thinker</h2>
      <span class="trait-icon" aria-hidden="true"><svg viewBox="0 0 30 30"><circle class="ring" cx="15" cy="15" r="14"/><path class="glyph" d="M11.5 17a5 5 0 1 1 7 0c-1 1-1.5 2-1.5 3h-4c0-1-.5-2-1.5-3zM13 23h4"/></svg></span>
      <ul class="trait-list">
        <li class="bulleted">I can ask questions like "why" and "how" to learn more about the world.</li>
        <li class="bulleted">When faced with a problem, I can be creative and come up<br>with different solutions.</li>
        <li class="bulleted">I can use facts and clues to help make wise decisions.</li>
      </ul>
    </section>

    <section class="trait trait--responsible">
      <h2 class="trait-name">Responsible</h2>
      <span class="trait-icon" aria-hidden="true"><svg viewBox="0 0 30 30"><circle class="ring" cx="15" cy="15" r="14"/><path class="glyph" d="M9 15.5l4 4 8-9"/></svg></span>
      <ul class="trait-list">
        <li class="bulleted">I can take ownership of my actions and remember to complete my job.<br>I can take care of my belongings and always try my best in schoolwork.<br>I can tell the truth and act with integrity even when no one is watching.</li>
      </ul>
    </section>

    <section class="trait trait--adaptable">
      <h2 class="trait-name">Adaptable</h2>
      <span class="trait-icon" aria-hidden="true"><svg viewBox="0 0 30 30"><circle class="ring" cx="15" cy="15" r="14"/><path class="glyph" d="M21 12a6.5 6.5 0 0 0-11.5-1M9 18a6.5 6.5 0 0 0 11.5 1M9.5 7v4h4M20.5 23v-4h-4"/></svg></span>
      <ul class="trait-list">
        <li class="bulleted">When a plan changes or a task is hard, I can stay calm and try a new way.</li>
        <li class="bulleted">I can learn from mistakes and use past knowledge to try new things.</li>
        <li class="bulleted">I can work and play well with people who are different from me.</li>
      </ul>
    </section>

    <section class="trait trait--collaborator">
      <h2 class="trait-name">Collaborator</h2>
      <span class="trait-icon" aria-hidden="true"><svg viewBox="0 0 30 30"><circle class="ring" cx="15" cy="15" r="14"/><circle class="glyph" cx="12" cy="15" r="5"/><circle class="glyph" cx="18" cy="15" r="5"/></svg></span>
      <ul class="trait-list">
        <li class="bulleted">I can share ideas and work together with a group to reach a common goal.</li>
        <li class="bulleted">I can listen to my teammates and respect their different ideas.</li>
        <li class="bulleted">I can know when to share, when to help others, and when to be the leader.</li>
      </ul>
    </section>

    <section class="trait trait--compassionate">
      <h2 class="trait-name">Compassionate</h2>
      <span class="trait-icon" aria-hidden="true"><svg viewBox="0 0 30 30"><circle class="ring" cx="15" cy="15" r="14"/><path class="solid" d="M15 22s-7-4.3-7-9a3.6 3.6 0 0 1 7-1.3A3.6 3.6 0 0 1 22 13c0 4.7-7 9-7 9z"/></svg></span>
      <ul class="trait-list">
        <li class="bulleted">I can be empathetic, noticing how others are feeling (happy, sad, frustrated).</li>
        <li class="bulleted">I can use kind words and gentle actions to support their friends.</li>
        <li class="bulleted">I can look for ways to help their school and the community.</li>
      </ul>
    </section>
  </main>
</body>
</html>
```